Apricot Variety Sheet - Meadowlark Orchard Co

We are needing a variety sheet that we can hand out that will describe the different apricot vatieties we have available. The attached document has the name of the variety along with a description that will need to be on the sheet. We are looking for a modern, appealing way to display this information on 1 page (if needed, it can be front and back)
Updates

Apologies for the delay; we are overwhelmed with the great design options and will be sorting through them all (across our contests) to pick a collective. Thank you for your patience.

Target Market(s)

Growers and consumers

Industry/Entity Type

Agriculture

Requirements
Must have
• Easy to read
• Natural color palettes to emphasize the agricultural nature
• Clearly show washington as the origin in the title or at the top
Nice to have
• incorporate Apricots in the design

```html
<!DOCTYPE html>
<html lang="en">
<head>
<meta charset="utf-8">
<title>Apricot Variety Sheet – Meadowlark Orchard Co, Washington State</title>
<link href="https://fonts.googleapis.com/css2?family=Lato:wght@300;400&family=Open+Sans:wght@300;400;600;700&display=swap" rel="stylesheet">
<style>
  :root {
    --paper: #ffffff;
    --brand-green: #1f6b3b;
    --title-green: #1e6a3c;
    --variety-red: #c4412f;
    --body-text: #333333;
    --band-dark: #1d5a2a;
    --band-lime: #8cc63f;
    --orchard-light: #9fd36a;
    --orchard-deep: #2f8a2c;
    --apricot-light: #f6a74a;
    --apricot-deep: #e0602a;
    --badge-orange: #f08a3a;
  }
  html, body {
    margin: 0;
    padding: 0;
    overflow: hidden;
  }
  body {
    width: 928px;
    height: 1200px;
    background: var(--paper);
  }
  .sheet {
    position: relative;
    width: 928px;
    height: 1200px;
    overflow: hidden;
    background: var(--paper);
    font-family: "Open Sans", sans-serif;
    color: var(--body-text);
  }
  .backdrop {
    position: absolute;
    inset: 0;
  }
  .brand {
    position: absolute;
    left: 56px;
    top: 34px;
    display: flex;
    align-items: center;
    gap: 22px;
  }
  .brand-dot {
    width: 124px;
    height: 124px;
    border-radius: 50%;
    background: var(--badge-orange);
    flex: none;
  }
  .brand-name {
    margin: 0;
    font-family: "Open Sans", sans-serif;
    font-weight: 700;
    font-size: 33px;
    line-height: 40px;
    color: var(--brand-green);
  }
  .sheet-title {
    position: absolute;
    left: 0;
    width: 680px;
    top: 190px;
    margin: 0;
    text-align: center;
    font-family: "Lato", sans-serif;
    font-weight: 300;
    font-size: 38px;
    letter-spacing: 0.5px;
    color: var(--title-green);
  }
  .variety-list {
    position: absolute;
    left: 44px;
    top: 275px;
  }
  .variety {
    margin-bottom: 12px;
  }
  .variety-name {
    margin: 0 0 8px;
    font-weight: 600;
    font-size: 26px;
    line-height: 34px;
    color: var(--variety-red);
  }
  .variety-text {
    margin: 0 0 0 18px;
    width: 600px;
    font-weight: 300;
    font-size: 17.5px;
    line-height: 28px;
    text-align: justify;
    hyphens: auto;
  }
  .variety--tomcot { margin-bottom: 22px; }
  .variety--tomcot .variety-text { width: 520px; text-align: left; }
  .variety--goldrich .variety-text { width: 400px; text-align: left; }
</style>
</head>
<body>
<main class="sheet">
  <svg class="backdrop" width="928" height="1200" viewBox="0 0 928 1200">
    <defs>
      <linearGradient id="orchardTone" x1="0" y1="0" x2="1" y2="1">
        <stop offset="0" stop-color="#9fd36a"/>
        <stop offset="0.5" stop-color="#2f8a2c"/>
        <stop offset="1" stop-color="#5faa3a"/>
      </linearGradient>
      <radialGradient id="apricotTone" cx="0.6" cy="0.5" r="0.7">
        <stop offset="0" stop-color="#f6a74a"/>
        <stop offset="1" stop-color="#e0602a"/>
      </radialGradient>
    </defs>
    <path class="orchard-photo" role="img" aria-label="Photo of a green Washington apricot orchard with rows of leafy trees on grass"
          d="M590 0 C680 140 730 330 742 520 C752 700 720 820 660 940 L928 940 L928 0 Z"
          fill="url(#orchardTone)"/>
    <path class="accent-band accent-band--dark"
          d="M560 0 C650 120 712 300 724 500 C734 660 712 800 664 930 L676 930 C724 800 748 660 740 500 C728 300 670 120 596 0 Z"
          fill="#1d5a2a"/>
    <path class="accent-band accent-band--lime"
          d="M596 0 C670 120 728 300 740 500 C748 660 724 800 676 930 L690 930 C738 800 760 660 752 500 C740 300 690 120 630 0 Z"
          fill="#8cc63f"/>
    <path class="apricot-photo" role="img" aria-label="Photo of a bowl heaped with ripe orange apricots beside green leaves"
          d="M400 1200 C430 1110 500 1030 600 990 C640 940 700 930 760 935 C820 900 880 905 928 915 L928 1200 Z"
          fill="url(#apricotTone)"/>
  </svg>

  <header class="brand">
    <div class="brand-dot" aria-hidden="true"></div>
    <p class="brand-name">Meadowlark Orchard Co<br>Washington State</p>
  </header>

  <h1 class="sheet-title">APRICOT VARIETY SHEET</h1>

  <div class="variety-list">
    <section class="variety variety--rival">
      <h2 class="variety-name">Rival</h2>
      <p class="variety-text">Great flavor with a fine, firm texture distinguishes this large oval-shaped apricot. The skin is light orange with a red blush. The flesh is a lush deep orange color. Available early July- early August.</p>
    </section>

    <section class="variety variety--robada">
      <h2 class="variety-name">Robada</h2>
      <p class="variety-text">This jumbo apricot has a delicious floral flavor with a firm texture. Bright orange, with a deep red blush over nearly half its surface. Available early June.</p>
    </section>

    <section class="variety variety--perfection">
      <h2 class="variety-name">Perfection</h2>
      <p class="variety-text">This classic large oval apricot is deep orange with an oblong shape and firm texture. The flesh is a yellow/orange color that is very sweet and full of flavor. Available mid July - mid August.</p>
    </section>

    <section class="variety variety--patterson">
      <h2 class="variety-name">Patterson</h2>
      <p class="variety-text">This apricot has a well-balanced flavor and an excellent shelf life. This is perfect for canning or drying. It has streaked red over yellow skin, with a firm flesh. Available mid – late June.</p>
    </section>

    <section class="variety variety--tomcot">
      <h2 class="variety-name">Tomcot</h2>
      <p class="variety-text">Tangy, sweet flavor with a firm texture. This oval apricot is light orange with a slight blush color. The flesh is a dark orange. Available late June – late July.</p>
    </section>

    <section class="variety variety--goldrich">
      <h2 class="variety-name">Goldrich</h2>
      <p class="variety-text">This apricot is round with a bright orange skin color and a deep orange flesh. It has a mild, sweet flavor with a firm texture. Available early July – mid August.</p>
    </section>
  </div>
</main>
</body>
</html>
```